Medical Marihuana Packaging Design

We seek skilled packaging designer for sales unit box for client of ours.

Unit is a metall tiin with outlay label in paper. The seeked design is: minimal, modern, coloring according to logo and ci of company (see attachment).

The product contained insales unit is medical marihuana which will be retailed to public.

Note: We dont need any marihuana leafs or signs. We need pharma related , moderm, serious, cutting edge design.

website: www.velmorastra.ch

Please check all attachments prior to posting ans questions, thx

Target Market(s)

young audience

Industry/Entity Type

Pharmaceutical

Font styles to use
Sans Serif

Colors
9bcb3c
acd037
cadf82
ffffff

Requirements
Must have
• Logo, corporate colors
Should not have
• No Marihuana Leafs or symbols

```html
<!DOCTYPE html>
<html lang="en">
<head>
<meta charset="utf-8">
<title>Velmorastra CBD Oil 20 Label</title>
<link href="https://fonts.googleapis.com/css2?family=Questrial&display=swap" rel="stylesheet">
<style>
  :root {
    --bg: #e6e6e6;
    --paper: #ffffff;
    --ink: #2b2521;
    --ink-soft: #4a4440;
    --accent-text: #5f9a6e;
    --green-deep: #3d8c3f;
    --green-olive: #6f9a3a;
    --green-pale: #cadf82;
    --green-lime: #9bcb3c;
    --green-leaf: #acd037;
    --grey-green: #5e7a66;
  }
  * { box-sizing: border-box; margin: 0; padding: 0; }
  html, body {
    width: 1091px; height: 1200px; overflow: hidden;
    background: var(--bg);
    font-family: "Questrial", "Helvetica Neue", Arial, sans-serif;
  }
  .label {
    position: absolute; left: 145px; top: 40px;
    width: 800px; height: 1120px;
    background: var(--paper);
    overflow: hidden;
    box-shadow: 0 6px 24px rgba(0,0,0,0.08);
  }
  .pattern-top {
    position: absolute; left: 0; top: 17px; width: 800px; height: 78px;
    background: linear-gradient(90deg, var(--green-deep), var(--green-olive) 35%, var(--green-pale) 75%, var(--grey-green));
  }
  .pattern-bottom {
    position: absolute; left: 0; top: 730px; width: 800px; height: 380px;
    background: linear-gradient(90deg, var(--green-deep), var(--green-lime) 55%, var(--green-pale));
  }
  .use-tag {
    position: absolute; left: 145px; top: 112px;
    font-size: 38px; letter-spacing: 3px; color: var(--ink-soft); line-height: 1;
  }
  .product-name {
    position: absolute; left: 140px; top: 255px;
    font-size: 136px; font-weight: 400; letter-spacing: 16px; color: var(--ink); line-height: 1;
  }
  .product-type {
    position: absolute; left: 362px; top: 490px;
    font-size: 72px; letter-spacing: 4px; color: var(--ink-soft); line-height: 1;
  }
  .product-strength {
    position: absolute; left: 528px; top: 440px;
    font-size: 60px; color: var(--accent-text); line-height: 1;
  }
  .brand {
    position: absolute; left: 14px; top: 820px;
    display: flex; align-items: center; gap: 14px;
  }
  .brand__dot { width: 60px; height: 60px; border-radius: 50%; background: var(--paper); }
  .brand__name { font-size: 44px; letter-spacing: 3px; color: var(--paper); }
  .content-info {
    position: absolute; right: 30px; top: 940px;
    font-size: 30px; letter-spacing: 1px; color: #2f4a2a; line-height: 1;
  }
  .volume {
    position: absolute; right: 30px; top: 985px;
    font-size: 46px; letter-spacing: 3px; color: var(--ink); line-height: 1;
  }
</style>
</head>
<body>
  <main class="label">
    <div class="pattern-top" role="img" aria-label="Decorative row of green colour blocks"></div>

    <p class="use-tag">SPECIFIC USE</p>
    <h1 class="product-name">CBD</h1>
    <p class="product-strength">20</p>
    <p class="product-type">OIL</p>

    <div class="pattern-bottom" role="img" aria-label="Decorative stacked green stripes"></div>

    <div class="brand">
      <span class="brand__dot"></span>
      <span class="brand__name">VELMORASTRA</span>
    </div>
    <p class="content-info">20% CBD (200 mg)</p>
    <p class="volume">10 mL</p>
  </main>
</body>
</html>
```